2024 Harwick Patrol Deputy's Statute Handbook

Cover, spine and back cover for our annual law manual. The overall size of the cover is 18.82 x 11 (with the .25 inch bleed it is 19.32 x 11.5) and the spine is 1.82 x 11 plus (1.82 x 11.5 with the bleed).
The book comes with a motor vehicle companion guide which will be 5" X 7" with spiral binding. The companion guide will have the same design with a slight twist related to motor vehicle law.

```html
<!DOCTYPE html>
<html lang="en">
<head>
<meta charset="utf-8">
<title>2024 Harwick Patrol Deputy's Statute Handbook – Cover Set</title>
<link rel="stylesheet" href="https://fonts.googleapis.com/css2?family=Archivo:wght@400;700;800;900&family=Black+Ops+One&family=Oswald:wght@500;600;700&display=swap">
<style>
  :root{
    --navy:#1f2048;
    --navy-deep:#0b0c3a;
    --gold:#f4ab35;
    --tape:#c99a1e;
    --tape-dark:#8a6a12;
    --red:#c8173d;
    --white:#ffffff;
    --paper:#ffffff;
  }
  html,body{margin:0;padding:0;overflow:hidden;background:var(--paper);}
  .canvas{position:relative;width:1200px;height:769px;overflow:hidden;background:var(--paper);font-family:"Archivo",Arial,sans-serif;}
  .panel{position:absolute;overflow:hidden;background:radial-gradient(ellipse at 40% 30%,#2a2b58 0%,var(--navy) 60%,#17183c 100%);}
  .spine{position:absolute;overflow:hidden;background:var(--navy-deep);}
  .year{position:absolute;font-family:"Black Ops One",Impact,sans-serif;color:var(--gold);line-height:1;letter-spacing:1px;}
  .title-red{position:absolute;color:var(--red);font-weight:800;line-height:1;white-space:nowrap;}
  .title-white{position:absolute;color:var(--white);font-weight:800;line-height:1;white-space:nowrap;}
  .brand{position:absolute;display:flex;flex-direction:column;align-items:center;gap:6px;color:var(--gold);font-weight:800;text-align:center;line-height:1.05;}
  .brand-dot{border-radius:50%;background:var(--gold);}
  .tape{position:absolute;background:var(--tape);border-top:3px solid var(--tape-dark);border-bottom:3px solid var(--tape-dark);display:flex;align-items:center;gap:150px;padding-left:14px;white-space:nowrap;font-family:"Oswald",Impact,sans-serif;font-weight:700;color:#15151f;box-sizing:border-box;}
  .state{position:absolute;font-family:"Oswald",Impact,sans-serif;font-weight:600;color:var(--red);line-height:1;text-align:right;white-space:nowrap;}
  .guide-to{position:absolute;color:var(--gold);font-weight:700;text-align:right;white-space:nowrap;line-height:1;}
  .topics{position:absolute;margin:0;padding:0;list-style:none;color:var(--white);text-align:right;font-weight:400;}
  .art{position:absolute;}
  .author{position:absolute;color:var(--white);font-weight:700;white-space:nowrap;text-align:center;}
  .spine-title{position:absolute;writing-mode:vertical-rl;color:var(--white);font-weight:800;line-height:1.05;white-space:nowrap;}
  .spine-guide{position:absolute;writing-mode:vertical-rl;line-height:1;white-space:nowrap;}
  .spine-guide .g-state{color:var(--gold);font-weight:800;}
  .spine-guide .g-sub{color:var(--gold);font-weight:400;}
  .spine-guide .g-big{color:var(--gold);font-weight:400;}
  .spine-author{position:absolute;left:0;right:0;text-align:center;color:var(--gold);white-space:nowrap;}
</style>
</head>
<body>
<div class="canvas">

  <!-- Main front cover -->
  <section class="panel" style="left:47px;top:42px;width:571px;height:679px;">
    <div class="year" style="left:38px;top:38px;font-size:96px;">2024</div>
    <div class="brand" style="left:430px;top:50px;width:120px;font-size:15px;">
      <span class="brand-dot" style="width:44px;height:44px;"></span>
      <span>KESTREL<br>PATROL<br>ACADEMY</span>
    </div>
    <div class="title-red" style="left:40px;top:140px;font-size:40px;">PATROL DEPUTY'S</div>
    <div class="title-white" style="left:40px;top:183px;font-size:42px;">STATUTE HANDBOOK</div>

    <div class="tape" style="left:-30px;top:288px;width:660px;height:40px;transform:rotate(-7.5deg);font-size:24px;">
      <span>POLICE LINE DO NOT CROSS</span><span>POLICE LINE DO NOT CROSS</span>
    </div>

    <svg class="art" role="img" aria-label="Bald eagle in front of a waving American flag" style="left:0;top:380px;" width="571" height="299" viewBox="0 0 571 299">
      <defs>
        <linearGradient id="flagMain" x1="0" y1="0" x2="1" y2="1">
          <stop offset="0" stop-color="#3a4a8c"/>
          <stop offset="0.35" stop-color="#c9cfdc"/>
          <stop offset="0.6" stop-color="#b3223d"/>
          <stop offset="1" stop-color="#e8e8ee"/>
        </linearGradient>
      </defs>
      <path d="M0 45 C120 25 230 45 330 85 C430 125 520 140 565 150 L540 260 C520 275 500 290 480 299 L0 299 Z" fill="url(#flagMain)"/>
    </svg>

    <div class="state" style="right:28px;top:368px;font-size:40px;">HARWICK</div>
    <div class="guide-to" style="right:28px;top:405px;font-size:14px;">PATROL DEPUTIES GUIDE TO</div>
    <ul class="topics" style="right:30px;top:424px;font-size:11px;line-height:14px;">
      <li>CRIMINAL PROCEDURE</li><li>STATUTORY LAW</li><li>MOTOR VEHICLE LAW</li><li>JUVENILE LAW</li>
    </ul>
    <div class="author" style="left:160px;width:370px;top:640px;font-size:18px;">Daniel R. Whitcombe, ESQ</div>
  </section>

  <!-- Main spine -->
  <section class="spine" style="left:629px;top:40px;width:108px;height:680px;">
    <div class="brand" style="left:0;width:108px;top:50px;font-size:11px;">
      <span class="brand-dot" style="width:30px;height:30px;"></span>
      <span>KESTREL<br>PATROL<br>ACADEMY</span>
    </div>
    <div class="year" style="left:0;width:108px;text-align:center;top:152px;font-size:30px;">2024</div>
    <div class="spine-title" style="left:22px;top:202px;font-size:22px;">PATROL DEPUTY'S<br>STATUTE HANDBOOK</div>
    <div class="spine-guide" style="left:28px;top:510px;">
      <span class="g-state" style="font-size:14px;">HARWICK</span><br>
      <span class="g-sub" style="font-size:12px;">PATROL DEPUTIES</span><br>
      <span class="g-big" style="font-size:26px;">GUIDE</span>
    </div>
    <div class="spine-author" style="top:662px;font-size:7.5px;">Daniel R. Whitcombe, ESQ</div>
  </section>

  <!-- Companion guide front -->
  <section class="panel" style="left:763px;top:287px;width:308px;height:431px;">
    <div class="art" role="img" aria-label="Faint car silhouette in the background" style="left:40px;top:15px;width:260px;height:170px;border-radius:40px;background:radial-gradient(ellipse at 60% 50%,rgba(120,124,170,0.35) 0%,rgba(31,32,72,0) 70%);"></div>
    <div class="year" style="left:20px;top:38px;font-size:46px;">2024</div>
    <div class="brand" style="left:222px;top:48px;width:70px;font-size:9px;">
      <span class="brand-dot" style="width:24px;height:24px;"></span>
      <span>KESTREL<br>PATROL<br>ACADEMY</span>
    </div>
    <div class="title-red" style="left:20px;top:90px;font-size:19px;">PATROL DEPUTY'S</div>
    <div class="title-white" style="left:20px;top:112px;font-size:22px;">MOTOR VEHICLE</div>
    <div class="title-white" style="left:20px;top:136px;font-size:32px;">LAW</div>

    <div class="tape" style="left:-15px;top:198px;width:340px;height:24px;transform:rotate(-6deg);font-size:14px;gap:70px;padding-left:22px;">
      <span>POLICE LINE DO NOT CROSS</span><span>POLICE LINE DO NOT CROSS</span>
    </div>

    <svg class="art" role="img" aria-label="Bald eagle in front of a waving American flag" style="left:0;top:255px;" width="308" height="176" viewBox="0 0 308 176">
      <defs>
        <linearGradient id="flagSmall" x1="0" y1="0" x2="1" y2="1">
          <stop offset="0" stop-color="#3a4a8c"/>
          <stop offset="0.35" stop-color="#c9cfdc"/>
          <stop offset="0.6" stop-color="#b3223d"/>
          <stop offset="1" stop-color="#e8e8ee"/>
        </linearGradient>
      </defs>
      <path d="M0 25 C70 15 130 28 185 50 C240 72 285 80 305 85 L290 150 C280 162 270 170 260 176 L0 176 Z" fill="url(#flagSmall)"/>
    </svg>

    <div class="state" style="right:26px;top:233px;font-size:22px;">HARWICK</div>
    <div class="guide-to" style="right:26px;top:256px;font-size:9px;">PATROL DEPUTIES GUIDE TO</div>
    <ul class="topics" style="right:27px;top:267px;font-size:7px;line-height:9px;">
      <li>CRIMINAL PROCEDURE</li><li>STATUTORY LAW</li><li>MOTOR VEHICLE LAW</li><li>JUVENILE LAW</li>
    </ul>
    <div class="author" style="left:70px;width:220px;top:409px;font-size:11px;">Daniel R. Whitcombe, ESQ</div>
  </section>

  <!-- Companion guide spine -->
  <section class="spine" style="left:1081px;top:287px;width:68px;height:431px;">
    <div class="brand" style="left:0;width:68px;top:30px;font-size:7px;gap:4px;">
      <span class="brand-dot" style="width:18px;height:18px;"></span>
      <span>KESTREL<br>PATROL<br>ACADEMY</span>
    </div>
    <div class="year" style="left:0;width:68px;text-align:center;top:93px;font-size:19px;">2024</div>
    <div class="spine-title" style="left:16px;top:128px;font-size:14px;">PATROL DEPUTY'S<br>MOTOR VEHICLE LAW</div>
    <div class="spine-guide" style="left:18px;top:320px;">
      <span class="g-state" style="font-size:8px;">HARWICK</span><br>
      <span class="g-sub" style="font-size:7px;">PATROL DEPUTIES</span><br>
      <span class="g-big" style="font-size:15px;">GUIDE</span>
    </div>
    <div class="spine-author" style="top:419px;font-size:4.5px;">Daniel R. Whitcombe, ESQ</div>
  </section>

</div>
</body>
</html>
```